curtainmaker, indoor and outdoor blind supplier

looking for logo to use for business cards and letter heads, I make all curtains for my clients and supply all kinds of blinds indoor and out. I'm looking for a design maybe with fabric background,

Industry/Entity Type

Business

Contact Information for Business Card

Moira Delaney Curtain Designs 14 Perriwick Drive Warrnambool 3280. phone 03 55847391 mobile 0428936054, email moiradelaneycurtaindesign@tarvomail.com website moiradelaneycurtaindesigns.example.au/

Requirements
Nice to have
• maybe something in relation to sewing as an option

```html
<!DOCTYPE html>
<html lang="en">
<head>
<meta charset="utf-8">
<title>Moira Delaney Curtain Designs – Business Cards</title>
<link rel="stylesheet" href="https://fonts.googleapis.com/css2?family=Crimson+Pro:wght@400;500&display=swap">
<style>
  :root {
    --page-bg: #ece6dc;
    --card-white: #ffffff;
    --ink: #1c1c1c;
    --band: #3a3836;
    --band-text: #f2f0ec;
    --fabric: #cdbf9f;
    --window-centre: #fbfaf6;
    --window-edge: #d8ccb0;
    --wood-light: #d39a62;
    --wood-dark: #b07440;
    --shadow: rgba(60, 45, 25, 0.25);
  }
  * { box-sizing: border-box; margin: 0; padding: 0; }
  html, body {
    width: 1200px; height: 900px; overflow: hidden;
    background: var(--page-bg);
    font-family: "Crimson Pro", Georgia, serif;
    color: var(--ink);
  }
  .canvas { position: relative; width: 1200px; height: 900px; }
  .card {
    position: absolute; left: 250px; width: 700px; height: 400px;
    background: var(--card-white);
    overflow: hidden;
    box-shadow: 0 10px 28px var(--shadow);
  }
  .card--front { top: 30px; }
  .card--back { top: 470px; }

  /* shared wordmark */
  .wordmark { display: inline-block; font-weight: 500; color: var(--ink); }
  .wordmark-name { display: block; line-height: 1; }
  .wordmark-sub { display: block; text-align: right; line-height: 1.1; }

  /* front card */
  .front-photo {
    position: absolute; inset: 0;
    background: radial-gradient(ellipse at 50% 45%, var(--window-centre) 30%, var(--window-edge) 100%);
  }
  .front-content {
    position: absolute; left: 150px; right: 140px; top: 118px;
    text-align: center;
  }
  .front-content .wordmark-name { font-size: 46px; }
  .front-content .wordmark-sub { font-size: 18px; }
  .tagline { margin-top: 14px; font-size: 22px; line-height: 1.2; }

  /* back card */
  .back-photo {
    position: absolute; left: 0; top: 0; width: 175px; height: 345px;
    background: var(--fabric);
  }
  .back-brand { position: absolute; left: 215px; top: 62px; }
  .back-brand .wordmark-name { font-size: 56px; }
  .back-brand .wordmark-sub { font-size: 20px; margin-top: 4px; }
  .contact-list {
    position: absolute; left: 208px; top: 180px;
    font-size: 20px; line-height: 27px;
  }
  .contact-row { display: flex; align-items: center; gap: 10px; }
  .contact-row .spacer { width: 50px; }
  .icon { width: 14px; height: 14px; flex: none; fill: var(--ink); }
  .info-band {
    position: absolute; left: 175px; right: 0; top: 268px; height: 77px;
    background: var(--band); color: var(--band-text);
  }
  .address {
    position: absolute; left: 20px; top: 12px; font-size: 20px; line-height: 25px;
  }
  .address .icon { fill: var(--band-text); margin-right: 8px; }
  .proprietor { position: absolute; right: 40px; top: 16px; text-align: center; }
  .proprietor-name { font-size: 26px; line-height: 28px; }
  .proprietor-role { font-size: 20px; line-height: 22px; }
  .floor {
    position: absolute; left: 0; right: 0; bottom: 0; height: 55px;
    background: linear-gradient(180deg, var(--wood-light), var(--wood-dark));
  }
</style>
</head>
<body>
<main class="canvas">

  <section class="card card--front" aria-label="Business card front">
    <div class="front-photo" role="img" aria-label="Photo of a lace-curtained window framed by cream damask drapes with gold tassel tie-backs"></div>
    <div class="front-content">
      <p class="wordmark"><span class="wordmark-name">Moira Delaney</span><span class="wordmark-sub">Curtain Designs</span></p>
      <p class="tagline">Curtains, blinds (indoor/outdoor)<br>all your window furnishing needs</p>
    </div>
  </section>

  <section class="card card--back" aria-label="Business card back">
    <div class="back-photo" role="img" aria-label="Photo of a cream damask curtain drawn back with a gold tassel tie-back"></div>
    <div class="back-brand">
      <p class="wordmark"><span class="wordmark-name">Moira Delaney</span><span class="wordmark-sub">Curtain Designs</span></p>
    </div>

    <div class="contact-list">
      <div class="contact-row">
        <svg class="icon" viewBox="0 0 16 16" aria-hidden="true"><path d="M4 1l3 3-2 2c1 2 3 4 5 5l2-2 3 3-2 2C7 14 2 9 2 3z"/></svg>
        <span>03 55847391</span>
        <span class="spacer"></span>
        <svg class="icon" viewBox="0 0 16 16" aria-hidden="true"><path d="M4 0h8v16H4zM5.5 2v10h5V2z"/></svg>
        <span>0428936054</span>
      </div>
      <div class="contact-row">
        <svg class="icon" viewBox="0 0 16 16" aria-hidden="true"><circle cx="8" cy="8" r="7" fill="none" stroke="#1c1c1c" stroke-width="1.6"/><path d="M1 8h14M8 1v14" stroke="#1c1c1c" stroke-width="1.4"/><ellipse cx="8" cy="8" rx="3" ry="7" fill="none" stroke="#1c1c1c" stroke-width="1.4"/></svg>
        <span>www.moiradelaneycurtaindesigns.example.au</span>
      </div>
      <div class="contact-row">
        <svg class="icon" viewBox="0 0 16 16" aria-hidden="true"><path d="M0 3h16v10H0zM1.5 4.5L8 9l6.5-4.5" stroke="#fff" stroke-width="1.2"/></svg>
        <span>moiradelaneycurtaindesign@tarvomail.com</span>
      </div>
    </div>

    <div class="info-band">
      <p class="address">
        <svg class="icon" viewBox="0 0 16 16" aria-hidden="true"><path d="M8 1l7 7h-2v7H9.5v-4h-3v4H3V8H1z"/></svg>14 Perriwick Drive<br>Warrnambool 3280
      </p>
      <div class="proprietor">
        <p class="proprietor-name">Moira Delaney</p>
        <p class="proprietor-role">Proprietor</p>
      </div>
    </div>
    <div class="floor" role="img" aria-label="Photo of polished timber floorboards"></div>
  </section>

</main>
</body>
</html>
```